Criação de Projeto Combo top of mind para Logística, Entrega & Armazenamento
A empresa queria:
" OFERECEMOS SERVIÇOS LOGISTICA COM TRANSPORTE DE CARGAS PESADAS, CARGAS FRACIONADAS E TRANSPORTE EXECUTIVO DE PASSAGEIROS E FRETAMENTO COM ONIBUS, VANS E MMICRO ONIBUS "

```html
<!DOCTYPE html>
<html lang="pt-BR">
<head>
<meta charset="UTF-8">
<title>KVL Locações e Transportes</title>
<link href="https://fonts.googleapis.com/css2?family=Barlow:wght@400;600;700;800;900&display=swap" rel="stylesheet">
<style>
  :root {
    --yellow: #f7c21a;
    --black: #0c0c0c;
    --white: #ffffff;
    --photo-dark: #2a2b22;
    --photo-mid: #6b6a52;
    --photo-light: #c9c2ad;
  }
  * { margin: 0; padding: 0; box-sizing: border-box; }
  html, body { width: 1200px; height: 1200px; overflow: hidden; background: var(--white); }
  .poster {
    position: relative;
    width: 1200px;
    height: 1200px;
    overflow: hidden;
    font-family: "Barlow", sans-serif;
  }
  .truck-photo {
    position: absolute;
    inset: 0 0 auto 0;
    height: 900px;
    background:
      radial-gradient(ellipse 420px 520px at 270px 470px, rgba(230,232,235,.85), transparent 70%),
      radial-gradient(ellipse 260px 260px at 640px 520px, rgba(210,210,205,.7), transparent 70%),
      radial-gradient(ellipse 200px 160px at 900px 520px, rgba(200,200,195,.6), transparent 70%),
      linear-gradient(180deg, var(--photo-light) 0%, var(--photo-mid) 45%, var(--photo-dark) 100%);
  }
  .shapes { position: absolute; inset: 0; }
  .headline {
    position: absolute;
    top: 82px;
    right: 64px;
    text-align: right;
    white-space: nowrap;
    color: var(--white);
    font-weight: 800;
    font-size: 44px;
    line-height: 54px;
    letter-spacing: 1px;
    text-transform: uppercase;
  }
  .headline-bar {
    position: absolute;
    top: 300px;
    right: 91px;
    width: 113px;
    height: 8px;
    background: var(--yellow);
  }
  .contact {
    position: absolute;
    left: 58px;
    top: 940px;
    color: var(--white);
  }
  .contact-label { font-weight: 800; font-size: 44px; line-height: 1.1; letter-spacing: .5px; }
  .contact-phone { font-weight: 800; font-size: 56px; line-height: 1.05; color: var(--yellow); }
  .contact-email { font-weight: 400; font-size: 26px; letter-spacing: 5px; margin-top: 8px; }
  .social { display: flex; gap: 26px; margin-top: 12px; font-size: 26px; font-weight: 400; }
  .social-item { display: flex; align-items: center; gap: 10px; }
  .social-dot { width: 30px; height: 30px; border-radius: 50%; background: var(--yellow); }
  .brand {
    position: absolute;
    left: 708px;
    top: 1005px;
  }
  .brand-row { display: flex; align-items: center; gap: 24px; }
  .brand-mark { width: 120px; height: 120px; border-radius: 50%; background: var(--yellow); }
  .brand-name { font-weight: 900; font-size: 140px; line-height: 1; color: var(--black); letter-spacing: 4px; }
  .brand-tagline {
    margin-top: 14px;
    margin-left: 40px;
    font-weight: 700;
    font-size: 24px;
    letter-spacing: 1px;
    color: var(--black);
    text-transform: uppercase;
  }
</style>
</head>
<body>
<div class="poster">
  <div class="truck-photo" role="img" aria-label="Três caminhões brancos enfileirados numa estrada ao pôr do sol, com floresta ao fundo"></div>

  <svg class="shapes" width="1200" height="1200" viewBox="0 0 1200 1200" aria-hidden="true">
    <polygon points="0,795 1200,468 1200,1200 0,1200" fill="var(--black)"/>
    <path d="M444 1200 C560 880 840 640 1200 564 L1200 636 C880 700 640 900 540 1200 Z" fill="var(--yellow)"/>
    <path d="M540 1200 C640 900 880 700 1200 636 L1200 1200 Z" fill="var(--white)"/>
  </svg>

  <h1 class="headline">Reference site about<br>lorem ipsum, giving<br>information on its origins,<br>as well as a random.</h1>
  <div class="headline-bar"></div>

  <div class="contact">
    <div class="contact-label">CONSULTE-NOS</div>
    <div class="contact-phone">00 99999-9999</div>
    <div class="contact-email">email@email.com.br</div>
    <div class="social">
      <span class="social-item"><span class="social-dot"></span>/seunome</span>
      <span class="social-item"><span class="social-dot"></span>/seunome</span>
    </div>
  </div>

  <div class="brand">
    <div class="brand-row">
      <span class="brand-mark"></span>
      <span class="brand-name">KVL</span>
    </div>
    <div class="brand-tagline">Locações e Transportes</div>
  </div>
</div>
</body>
</html>
```